Dubai Family protection infographic

We need to produce a way of attracting people to a life insurance and critical illness cover seminar. As this is a pretty dull subject for most people, so we need a cool way of getting people to read the invite/marketing collateral.

We're thinking some kind of colourful and attractive infographic that we can use on flyers and posters as well as online and as an emailer.

Content for the graphic is as bellow:

How much does it cost to replace Mum & Dad?

Mum = Chauffer, Cook, Laundry Service, Household Cleaner, Psychologist, Money Manager

Mums typically work a 94-hour week. At a rather paltry $12 per hour, that’s $4,888 per month – or $58,656 each year. (Source: wagelore.net)

Dad : The average Western Expat’s salary in the Gulf is $12,215 per month. That’s $146,580 each year. (Source: Palmcrest Ledger).

Did you know that the average age of critical illness claimants in the Middle East last year was just 48. Of these, 44% were for cancer while 41% were heart related.

The average age of a death claimant was just 50 years old.
(Source: Verenholt Assurance Group)

1 in 3 people will develop some form of cancer during their lifetime.

That’s 2.36 billion people globally.

And that’s equivalent to the population of China, USA, Brazil, Russia, Philippines, France, UK, South Africa and Italy combined.

Does your family have the resources to hand to cope if a tragedy happens to you?

What can you do to protect them and yourself?

Come to the UAE’s first national protection seminar to find out. Join us at Harbourline Riverside Sports Arena on June 19th at 19:00.

To pre-register, visit www.tovanmere.net/events or alternatively register on the door.

```html
<!DOCTYPE html>
<html lang="en">
<head>
<meta charset="utf-8">
<title>How Much Does It Cost To Replace Mum &amp; Dad?</title>
<link rel="stylesheet" href="https://fonts.googleapis.com/css2?family=Arimo:wght@400;700&family=Bangers&family=Libre+Franklin:wght@800&display=swap">
<style>
  :root {
    --paper: #ffffff;
    --frame: #9a9a9a;
    --ink: #1a1a1a;
    --body-grey: #3c3c3c;
    --band-yellow: #f2ea2a;
    --band-orange: #f39a24;
    --band-pink: #f6a3c4;
    --band-blue: #7dcdf0;
    --band-grey: #e4e4e4;
    --ribbon-red: #d7191f;
    --ribbon-dark: #8e0e12;
    --headline-white: #ffffff;
    --headline-cyan: #2ec4ee;
    --headline-outline: #1b1b1b;
  }
  * { margin: 0; padding: 0; box-sizing: border-box; }
  html, body { width: 860px; height: 1200px; overflow: hidden; background: var(--paper); }
  .poster {
    position: relative; width: 860px; height: 1200px;
    background: var(--paper); border: 1px solid var(--frame);
    font-family: "Arimo", Arial, sans-serif; color: var(--body-grey);
  }
  .family-photo {
    position: absolute; left: 10px; top: 10px; width: 840px; height: 492px;
    background: linear-gradient(160deg, #efe6da 0%, #e2cdb3 35%, #caa689 60%, #e9dfd3 100%);
  }
  .headline {
    position: absolute; left: 58px; top: 400px;
    font-family: "Bangers", "Impact", sans-serif; font-style: italic;
    color: var(--headline-white);
    -webkit-text-stroke: 1.5px var(--headline-outline);
    text-shadow: 2px 2px 0 var(--headline-outline);
    transform: rotate(-3deg); transform-origin: left top;
    line-height: 0.95; letter-spacing: 1px;
  }
  .headline .line-1 { display: block; font-size: 40px; padding-left: 22px; }
  .headline .line-2 { display: block; font-size: 30px; }
  .headline .line-3 { display: block; font-size: 56px; color: var(--headline-cyan); padding-left: 116px; }
  .bands { position: absolute; left: 0; top: 0; width: 860px; height: 1200px; pointer-events: none; }
  .band-copy { position: absolute; left: 10px; width: 840px; text-align: center; color: var(--body-grey); }
  .mum-copy { top: 574px; font-size: 16px; line-height: 26px; transform: rotate(-1.5deg); }
  .dad-copy { top: 670px; font-size: 16px; line-height: 24px; transform: rotate(0.4deg); }
  .role { font-weight: 700; font-size: 19px; color: #2a2a2a; }
  .source { font-size: 12px; }
  .facts { position: absolute; left: 30px; top: 742px; width: 800px; text-align: center; font-size: 15.5px; line-height: 21px; }
  .facts p { margin-bottom: 10px; }
  .facts p.tight { margin-bottom: 2px; }
  .question-band {
    position: absolute; left: 10px; top: 944px; width: 840px; height: 72px;
    background: var(--band-grey);
    font-family: "Libre Franklin", Arial, sans-serif; font-weight: 800;
    color: var(--ink); font-size: 16px; line-height: 25px; text-align: center; padding-top: 11px;
  }
  .invite { position: absolute; left: 10px; width: 840px; text-align: center; color: var(--ink); font-weight: 700; }
  .invite-lead { top: 1024px; font-size: 16px; line-height: 22px; }
  .ribbon-bar {
    position: absolute; left: 100px; top: 1068px; width: 660px; height: 36px;
    background: linear-gradient(180deg, var(--ribbon-red) 0%, #b8141a 100%);
    color: #fff; font-size: 17.5px; font-weight: 400; line-height: 36px; text-align: center;
  }
  .ribbon-bow { position: absolute; top: 1040px; width: 96px; height: 96px; background: var(--ribbon-dark); border-radius: 6px; }
  .ribbon-bow.left { left: 16px; }
  .ribbon-bow.right { right: 16px; }
  .register { top: 1118px; font-size: 16.5px; line-height: 24px; }
</style>
</head>
<body>
<div class="poster">
  <div class="family-photo" role="img" aria-label="Photograph of a smiling three-generation family: grandparents, parents and two children gathered together on a sofa"></div>

  <svg class="bands" viewBox="0 0 860 1200" aria-hidden="true">
    <polygon points="10,507 850,501 850,541 10,548" fill="var(--band-yellow)"/>
    <polygon points="800,534 850,530 850,548 790,548" fill="var(--band-orange)"/>
    <polygon points="10,576 850,552 850,641 10,663" fill="var(--band-pink)"/>
    <polygon points="10,668 850,673 850,726 10,717" fill="var(--band-blue)"/>
  </svg>

  <h1 class="headline">
    <span class="line-1">HOW MUCH</span>
    <span class="line-2">DOES IT COST TO REPLACE</span>
    <span class="line-3">MUM &amp; DAD?</span>
  </h1>

  <p class="band-copy mum-copy">
    <span class="role">Mum</span> = Chauffer, Cook, Laundry Service, Household Cleaner, Psychologist, Money Manager.<br>
    Mums typically work a 94-hour week. At a rather paltry $12 per hour, that’s $4,888 per month<br>
    or $58,656 each year. <span class="source">(Source: wagelore.net)</span>
  </p>

  <p class="band-copy dad-copy">
    <span class="role">Dad</span> : The average Western Expat’s salary in the Gulf is $12,215 per month.<br>
    That’s $146,580 each year. <span class="source">(Source: Palmcrest Ledger)</span>
  </p>

  <div class="facts">
    <p>Did you know that the average age of critical illness claimants in the Middle East last year was just 48.<br>Of these, 44% were for cancer while 41% were heart related.</p>
    <p class="tight">The average age of a death claimant was just 50 years old.</p>
    <p><span class="source">(Source: Verenholt Assurance Group)</span></p>
    <p class="tight">1 in 3 people will develop some form of cancer during their lifetime.</p>
    <p class="tight">That’s 2.36 billion people globally.</p>
    <p>And that’s equivalent to the population of China, USA, Brazil, Russia,<br>Philippines, France, UK, South Africa and Italy combined.</p>
  </div>

  <div class="question-band">
    Does your family have the resources to hand to cope if a tragedy happens to you?<br>
    What can you do to protect them and yourself?
  </div>

  <p class="invite invite-lead">Come to the<br>UAE’s First National Protection Seminar To Find Out.</p>

  <div class="ribbon-bow left" role="img" aria-label="Red ribbon bow decoration"></div>
  <div class="ribbon-bow right" role="img" aria-label="Red ribbon bow decoration"></div>
  <p class="ribbon-bar">Join us at Harbourline Riverside Sports Arena on June 19th, 2013 at 19:00.</p>

  <p class="invite register">To pre-register,<br>visit www.tovanmere.net/events or alternatively register on the door.</p>
</div>
</body>
</html>
```